Re-style home page - eye-catching and unique design for social commerce website

We need a new concept design for TrindaMo's home page.
We don't want to make huge changes but creating a more professional and eye-catching style.

We need to look very serious like a professional services company and in the same time to look like a social network for e-commerce.

Our logo is very captive and you can use to creating something of harmonious.

This is a re-style and I'm excepted to see unique and fresh design like Clovaret.

Target Market(s)

e-commerce and social

Industry/Entity Type

Social

Number of Pages Required

1 page

Font styles to use
Serif
Sans Serif

Requirements
Must have
• An eye-catching result.
• Search bar with logo and Login How it works and business
• The slogan with login and signup.
• Footer links.
Nice to have
• I would like to open the home page and see only two clear ways:
• -Consumer
• --Search
• --The slogan
• --Login and Signup
• --How it works
• -Business
• --Go to Business area
• Background: City, Shopping.
Should not have
• Scrollbar style!

```html
<!DOCTYPE html>
<html lang="en">
<head>
<meta charset="utf-8">
<title>TrindaMo — Shop directly from your profile</title>
<link rel="stylesheet" href="https://fonts.googleapis.com/css2?family=Montserrat:wght@400;600;700&family=Open+Sans:wght@300;400&display=swap">
<style>
  :root {
    --night: #1c1d4a;
    --dusk: #4a4a86;
    --haze: #7a7092;
    --header-bg: rgba(22, 24, 60, 0.72);
    --white: #ffffff;
    --field-text: #3a3a3a;
    --placeholder: #8a8a8a;
    --chevron: #b5b5b5;
    --signup: #d32f2f;
    --business: #7cb82f;
    --map-blue: #8fb6dc;
  }
  * { box-sizing: border-box; margin: 0; padding: 0; }
  html, body { width: 1200px; height: 675px; overflow: hidden; }
  body {
    position: relative;
    font-family: "Montserrat", sans-serif;
    color: var(--white);
    background: var(--night);
  }
  .city-backdrop {
    position: absolute; inset: 0;
    background:
      radial-gradient(ellipse at 20% 35%, rgba(140, 110, 120, 0.55), transparent 55%),
      radial-gradient(ellipse at 78% 30%, rgba(150, 150, 190, 0.45), transparent 55%),
      linear-gradient(180deg, var(--dusk) 0%, var(--haze) 45%, #3b3565 75%, var(--night) 100%);
  }
  .site-header {
    position: absolute; left: 0; top: 0; width: 1200px; height: 59px;
    background: var(--header-bg);
  }
  .brand {
    position: absolute; left: 25px; top: 14px;
    display: flex; align-items: center; gap: 8px;
    font-family: "Montserrat", sans-serif; font-weight: 600; font-size: 27px;
    color: var(--white); line-height: 1;
  }
  .brand-mark { width: 18px; height: 18px; background: var(--white); }
  .feed-label {
    position: absolute; left: 295px; top: 22px;
    font-size: 11px; font-weight: 700;
  }
  .feed-select {
    position: absolute; top: 12px; height: 34px; width: 176px;
    background: var(--white); border-radius: 3px;
    font-family: "Open Sans", sans-serif; font-size: 12px; color: var(--field-text);
    display: flex; align-items: center; padding-left: 12px;
  }
  .feed-select svg.chevron { position: absolute; right: 12px; top: 14px; }
  .feed-interest { left: 399px; }
  .feed-city { left: 584px; padding-left: 28px; }
  .feed-city svg.pin { position: absolute; left: 11px; top: 10px; }
  .signup-button {
    position: absolute; left: 773px; top: 12px; width: 84px; height: 35px;
    background: var(--signup); border-radius: 3px;
    display: flex; align-items: center; justify-content: center;
    font-size: 13px; font-weight: 600;
  }
  .login-link { position: absolute; left: 871px; top: 21px; font-size: 13px; font-weight: 600; }
  .community-graphic {
    position: absolute; left: 466px; top: 127px; width: 263px; height: 163px;
    border-radius: 12px;
    background: radial-gradient(ellipse at 50% 75%, rgba(143, 182, 220, 0.55), rgba(255, 255, 255, 0.12) 60%, transparent 80%);
  }
  .slogan {
    position: absolute; left: 0; width: 1200px; top: 312px; text-align: center;
    font-family: "Open Sans", sans-serif; font-weight: 300; font-size: 33px;
  }
  .search-field {
    position: absolute; left: 437px; top: 372px; width: 325px; height: 41px;
    background: var(--white); border-radius: 2px;
    font-family: "Open Sans", sans-serif; font-size: 13px; color: var(--placeholder);
    display: flex; align-items: center; padding-left: 17px;
  }
  .search-icon { position: absolute; left: 778px; top: 385px; }
  .business-button {
    position: absolute; left: 511px; top: 435px; width: 179px; height: 34px;
    background: var(--business); border-radius: 2px;
    display: flex; align-items: center; justify-content: center; gap: 8px;
    font-size: 12px; font-weight: 600;
  }
  .how-it-works {
    position: absolute; left: 0; width: 1200px; top: 481px; text-align: center;
    font-size: 11px; font-weight: 600;
  }
  .footer-links {
    position: absolute; left: 0; width: 1200px; top: 575px;
    display: flex; justify-content: center; gap: 26px;
    font-size: 10.5px; font-weight: 600; list-style: none;
  }
  .copyright {
    position: absolute; left: 0; width: 1200px; top: 603px; text-align: center;
    font-size: 9.5px; font-weight: 600;
  }
</style>
</head>
<body>
  <div class="city-backdrop" role="img" aria-label="Blurred photograph of a busy city shopping street with crowds of people"></div>

  <header class="site-header">
    <div class="brand"><span>TrindaMo</span><span class="brand-mark"></span></div>
    <span class="feed-label">Setup your feed</span>
    <div class="feed-select feed-interest">Active life
      <svg class="chevron" width="12" height="7" viewBox="0 0 12 7"><path d="M1 1l5 5 5-5" fill="none" stroke="var(--chevron)" stroke-width="1.3"/></svg>
    </div>
    <div class="feed-select feed-city">
      <svg class="pin" width="10" height="14" viewBox="0 0 10 14"><path d="M5 0a5 5 0 0 0-5 5c0 4 5 9 5 9s5-5 5-9a5 5 0 0 0-5-5zm0 7a2 2 0 1 1 0-4 2 2 0 0 1 0 4z" fill="var(--chevron)"/></svg>
      London
      <svg class="chevron" width="12" height="7" viewBox="0 0 12 7"><path d="M1 1l5 5 5-5" fill="none" stroke="var(--chevron)" stroke-width="1.3"/></svg>
    </div>
    <div class="signup-button">Sign Up</div>
    <span class="login-link">Login</span>
  </header>

  <div class="community-graphic" role="img" aria-label="Illustration of four member avatars connected by dotted lines to a folded map"></div>

  <h1 class="slogan">Shop directly from your profile</h1>

  <div class="search-field">Search keyword</div>
  <svg class="search-icon" width="20" height="20" viewBox="0 0 20 20"><circle cx="8" cy="8" r="6" fill="none" stroke="var(--white)" stroke-width="2.6"/><path d="M12.5 12.5l5.5 5.5" stroke="var(--white)" stroke-width="2.8" stroke-linecap="round"/></svg>

  <div class="business-button">Go to Business Area
    <svg width="18" height="8" viewBox="0 0 18 8"><path d="M0 4h16M13 1l3 3-3 3" fill="none" stroke="var(--white)" stroke-width="1"/></svg>
  </div>
  <div class="how-it-works">How it works</div>

  <ul class="footer-links">
    <li>About Us</li><li>Blog</li><li>Business</li><li>Jobs</li><li>Privacy</li><li>FAQ</li><li>Contacts</li>
  </ul>
  <p class="copyright">© 2015 TrindaMo. All right reserved.</p>
</body>
</html>
```